Financial Broker firm looking for Brochure design/Pdf-document

Job Type
Brochure Design/PDF-Document
Task Outline
Create a Brochure Design that also works for sending as pdf-document.
Task Description
We need a combined corporate brochure (Booklet style) to give out to potential clients as well as sending it to potential clients through Internet as pdf-document.
We need a background template with pictures and colors that gives the impression of professionalism, trustworthiness and seriousness. Attached text in English but the text will be translated into different languages to fit different markets. Therefore we would like to receive one template including the text and one without any text (but with the logo). Please inform us where (any) pictures and/or photos on the template have been taken from in order for us to buy and use them legally.
About Us
Our company Quelvant Partners AB is a financial brokerage company who provides a diversity of services for different selected partners (www.quelvantpartners.example).
Target Market
Companies on all levels, domestic or international
Requirements
Must Have:
-The text and logo attached below
Industry/Entity Type
Financial
Look and feel

```html
<!DOCTYPE html>
<html lang="en">
<head>
<meta charset="utf-8">
<title>Quelvant Partners – Brochure Cover</title>
<link rel="stylesheet" href="https://fonts.googleapis.com/css2?family=PT+Sans:wght@400;700&display=swap">
<style>
  :root {
    --teal: #2c6278;
    --teal-low: #2d6a78;
    --blue-deep: #0b86bd;
    --blue-light: #2fb2e6;
    --divider: #1f6f93;
    --red: #d3232a;
    --red-dark: #7a1418;
    --ink: #111111;
    --white: #ffffff;
    --paper: #ffffff;
  }
  html, body {
    margin: 0;
    padding: 0;
    width: 1200px;
    height: 1000px;
    overflow: hidden;
    background: var(--paper);
  }
  .cover {
    position: relative;
    width: 1200px;
    height: 1000px;
    font-family: "PT Sans", Arial, sans-serif;
  }
  .cover-art {
    position: absolute;
    left: 0;
    top: 0;
    width: 1200px;
    height: 1000px;
  }
  .brand-name {
    position: absolute;
    left: 40px;
    top: 228px;
    margin: 0;
    font-size: 56px;
    font-weight: 700;
    letter-spacing: 1px;
    color: var(--ink);
    line-height: 1;
  }
  .tagline {
    position: absolute;
    left: 30px;
    top: 296px;
    margin: 0;
    font-size: 35px;
    font-weight: 400;
    color: var(--white);
    line-height: 1;
  }
  .contact-person {
    position: absolute;
    right: 12px;
    top: 324px;
    margin: 0;
    text-align: right;
    font-size: 19px;
    line-height: 22px;
    color: var(--white);
  }
  .contact-address {
    position: absolute;
    left: 653px;
    top: 726px;
    margin: 0;
    font-style: normal;
    font-size: 18px;
    line-height: 21px;
    color: var(--white);
  }
</style>
</head>
<body>
<main class="cover">
  <svg class="cover-art" viewBox="0 0 1200 1000" xmlns="http://www.w3.org/2000/svg">
    <defs>
      <linearGradient id="flap-blue" x1="0" y1="0" x2="1" y2="0">
        <stop offset="0" stop-color="var(--blue-deep)"/>
        <stop offset="0.5" stop-color="var(--blue-light)"/>
        <stop offset="1" stop-color="var(--blue-deep)"/>
      </linearGradient>
      <linearGradient id="ground" x1="0" y1="0" x2="0" y2="1">
        <stop offset="0" stop-color="var(--teal)"/>
        <stop offset="1" stop-color="var(--teal-low)"/>
      </linearGradient>
      <linearGradient id="arrow-left" x1="0" y1="1" x2="1" y2="0">
        <stop offset="0" stop-color="var(--red-dark)"/>
        <stop offset="0.45" stop-color="var(--red)"/>
      </linearGradient>
      <linearGradient id="arrow-right" x1="1" y1="1" x2="0" y2="0">
        <stop offset="0" stop-color="var(--red-dark)"/>
        <stop offset="0.45" stop-color="var(--red)"/>
      </linearGradient>
      <linearGradient id="device-tone" x1="0" y1="0" x2="1" y2="1">
        <stop offset="0" stop-color="#5d6d7b"/>
        <stop offset="0.55" stop-color="#9aa7b2"/>
        <stop offset="1" stop-color="#1c2127"/>
      </linearGradient>
      <filter id="soft-shadow" x="-10%" y="-10%" width="120%" height="130%">
        <feDropShadow dx="0" dy="4" stdDeviation="4" flood-color="#000" flood-opacity="0.45"/>
      </filter>
    </defs>

    <rect class="ground" x="0" y="0" width="1200" height="925" fill="url(#ground)"/>

    <g class="top-flaps" filter="url(#soft-shadow)">
      <path d="M0,0 H592 V240 Q330,70 0,0 Z" fill="url(#flap-blue)"/>
      <path d="M610,0 H1200 V0 Q880,60 610,240 Z" fill="url(#flap-blue)"/>
    </g>
    <rect class="spine" x="592" y="0" width="18" height="240" fill="var(--divider)"/>

    <g class="bottom-flap" filter="url(#soft-shadow)">
      <path d="M0,686 Q300,880 600,922 Q900,880 1200,676 V925 H0 Z" fill="url(#flap-blue)"/>
    </g>

    <g class="arrows" filter="url(#soft-shadow)">
      <path d="M5,606 Q260,540 445,410 L405,352 L528,378 L512,512 L475,448 Q270,560 5,606 Z" fill="url(#arrow-left)"/>
      <path d="M1190,606 Q930,540 750,410 L790,352 L667,378 L684,512 L722,448 Q925,560 1190,606 Z" fill="url(#arrow-right)"/>
    </g>

    <polygon class="business-photo" role="img"
      aria-label="Photo of a businessman touching a tablet screen showing a bar and line chart"
      points="150,598 535,766 480,905 88,735" fill="url(#device-tone)"/>
  </svg>

  <h1 class="brand-name">QUELVANT PARTNERS</h1>
  <p class="tagline">“A partner in need as in success”</p>

  <p class="contact-person">
    Contacted by:<br>
    Henrik Dalmore-Vasseur<br>
    Tel: +46705550142
  </p>

  <address class="contact-address">
    Contact Adress:<br>
    Quelvant Partners AB<br>
    Norrbrogatan 12<br>
    211 40 Malmö<br>
    Sweden<br>
    www.quelvantpartners.example
  </address>
</main>
</body>
</html>
```